Need a simple buisness card for my plumbing business. Would like it to be black background with white text.

Industry/Entity Type

Business

Requirements
Must have
• On the front of the card I need to have,
TKB PLUMBING SERVICES
PLUMBERS, DRAINERS & GASFITTERS
Dorian Wellsby
0471596083
Info@tkbplumbingservices.com.au
LIC No 517483f
ABN No 61907354218
On the back I need in point form
Domestic,industrial,commercial, all new installations, renovations, sewer renewals, repairs,
Fully licensed and insured
Nice to have
• A nice simple logo

```html
<!DOCTYPE html>
<html lang="en">
<head>
<meta charset="utf-8">
<title>TKB Plumbing Services – Business Card</title>
<link rel="stylesheet" href="https://fonts.googleapis.com/css2?family=Francois+One&display=swap">
<style>
  :root {
    --page-bg: #ececec;
    --card-bg: #000000;
    --ink: #ffffff;
    --divider-glow: #d9d9d9;
  }
  * { box-sizing: border-box; margin: 0; padding: 0; }
  html, body {
    width: 1200px;
    height: 900px;
    overflow: hidden;
    background: var(--page-bg);
  }
  body {
    position: relative;
    font-family: "Francois One", "Arial Narrow", sans-serif;
    color: var(--ink);
  }
  .card {
    position: absolute;
    width: 640px;
    height: 380px;
    background: var(--card-bg);
  }
  .card--front { left: 80px; top: 50px; }
  .card--back { left: 460px; top: 470px; }

  /* Front */
  .brand {
    position: absolute;
    left: 20px;
    top: 150px;
    width: 290px;
    text-align: center;
    line-height: 1.1;
  }
  .brand__mark {
    display: block;
    width: 44px;
    height: 44px;
    margin: 0 auto 14px;
    border-radius: 50%;
    background: var(--ink);
  }
  .brand__name { font-size: 19px; letter-spacing: 0.3px; }
  .brand__tagline { font-size: 16px; }

  .divider {
    position: absolute;
    left: 318px;
    top: 50px;
    width: 3px;
    height: 270px;
    background: linear-gradient(to bottom, transparent, var(--divider-glow) 25%, var(--ink) 50%, var(--divider-glow) 75%, transparent);
  }
  .contact {
    position: absolute;
    left: 360px;
    top: 58px;
  }
  .contact__name { font-size: 26px; letter-spacing: 0.5px; margin-bottom: 38px; }
  .contact__list { list-style: none; font-size: 14px; line-height: 1.45; }

  /* Back */
  .back-brand {
    position: absolute;
    left: 0;
    right: 0;
    top: 40px;
    text-align: center;
    line-height: 1.1;
  }
  .back-brand__mark {
    display: block;
    width: 70px;
    height: 70px;
    margin: 0 auto 22px;
    border-radius: 50%;
    background: var(--ink);
  }
  .back-brand__name { font-size: 32px; letter-spacing: 0.5px; }
  .back-brand__tagline { font-size: 32px; letter-spacing: 0.5px; }

  .services {
    position: absolute;
    top: 268px;
    list-style: none;
    font-size: 14px;
    line-height: 1.25;
  }
  .services li::before { content: "•"; margin-right: 8px; }
  .services--left { left: 80px; }
  .services--right { left: 360px; top: 286px; }
</style>
</head>
<body>
  <section class="card card--front" aria-label="Card front">
    <div class="brand">
      <span class="brand__mark"></span>
      <div class="brand__name">TKB PLUMBING SERVICES</div>
      <div class="brand__tagline">PLUMBERS, DRAINERS &amp; GASFITTERS</div>
    </div>
    <div class="divider"></div>
    <div class="contact">
      <h1 class="contact__name">Dorian Wellsby</h1>
      <ul class="contact__list">
        <li>0471596083</li>
        <li>Info@tkbplumbingservices.com.au</li>
        <li>LIC No 517483f</li>
        <li>ABN No 61907354218</li>
      </ul>
    </div>
  </section>

  <section class="card card--back" aria-label="Card back">
    <div class="back-brand">
      <span class="back-brand__mark"></span>
      <div class="back-brand__name">TKB PLUMBING SERVICES</div>
      <div class="back-brand__tagline">PLUMBERS, DRAINERS &amp; GASFITTERS</div>
    </div>
    <ul class="services services--left">
      <li>Domestic</li>
      <li>Industrial</li>
      <li>Commercial</li>
      <li>All new installations</li>
    </ul>
    <ul class="services services--right">
      <li>Renovations</li>
      <li>Sewer renewals</li>
      <li>Repairs</li>
      <li>Fully licensed and insured</li>
    </ul>
  </section>
</body>
</html>
```